THORNWICK COVE RUM - Premium Gold Rum Needs New Label

We would like a better label that we currently have for our Gold Rum that won the bronze medal in the 2003 Velmora Spirits Gala. We have called it "Thornwick Cove Rum" as our distillery is based here in Golden bay, New Zealand. The first recorded siting of New Zealand was made by Corin Velde and while anchored in the bay erupted in a terrible bloodshed with the natives. Corin Velde and his crew fled without setting foot on land. See attached back label for more on this story or google it! We have only a few thousand litres of the award winning rum and once sold out intend to import rum from Barbados and continue to sell it as "Thornwick Cove Rum" so the award winning aspect will be lost. We do not wish to change the label at that time but instead simply use stickers on the bottles containing the award winning rum and once sold out of the award running rum continue without the stickers. I think that there is a lot of imagery to draw and that the name is great! We want to see it in all the cool bars and bottle stores in New Zealand and Australia. It will be a premium product but we do not want to use a bespoke bottle. I attach pictures of our existing bottle and label and also dimensions and specs of the bottle that we will be using going forward. The bottle is the "quill" bottle - see numbers 3 and 4 on the attached spec sheet. We will most likely use with a cork ie bottle 4.
Target Market(s)
Up and coming professional males, 25-35, the cool cats who drink at the cool bars.
Requirements
Must have
- Must state: 40% ALC/VOL, Bottled by: Pellow Finch Distillery, 17b Harrowgate Lane, Takaka, Golden Bay, New Zealand, bar code Must also have some embossing/texture on the label
Should not have
- See "Grimwald Rum" - recently released - let's not look like them please.

```html
<!DOCTYPE html>
<html lang="en">
<head>
<meta charset="utf-8">
<title>Thornwick Cove Gold Rum – Label</title>
<link href="https://fonts.googleapis.com/css2?family=Almendra:wght@400;700&family=Cormorant+Garamond:ital,wght@0,500;0,600;1,500&display=swap" rel="stylesheet">
<style>
  :root {
    --ink: #0a0706;
    --gold: #c9a227;
    --gold-soft: #b8922a;
    --gold-deep: #8a6a18;
    --cream: #f5efe0;
    --page: #ffffff;
  }
  html, body {
    margin: 0;
    padding: 0;
    width: 1200px;
    height: 1000px;
    overflow: hidden;
    background: var(--page);
  }
  .canvas {
    position: relative;
    width: 1200px;
    height: 1000px;
  }
  .label {
    position: absolute;
    left: 185px;
    top: 54px;
    width: 830px;
    height: 892px;
  }
  .label-shapes {
    position: absolute;
    inset: 0;
  }
  .brand-name {
    position: absolute;
    left: 0;
    top: 50px;
    width: 830px;
    text-align: center;
    font-family: "Almendra", serif;
    font-weight: 700;
    font-size: 108px;
    line-height: 1;
    color: var(--cream);
    letter-spacing: 1px;
  }
  .product-type {
    position: absolute;
    left: 235px;
    top: 182px;
    width: 363px;
    height: 78px;
    display: flex;
    align-items: center;
    justify-content: center;
    font-family: "Almendra", serif;
    font-weight: 700;
    font-size: 50px;
    color: var(--cream);
  }
  .emblem-art {
    position: absolute;
    left: 45px;
    top: 262px;
    width: 375px;
    height: 610px;
  }
  .story {
    position: absolute;
    left: 442px;
    top: 392px;
    width: 325px;
  }
  .story-kicker {
    font-family: "Cormorant Garamond", serif;
    font-weight: 500;
    font-size: 24px;
    letter-spacing: 1px;
    color: var(--gold);
    margin: 0 0 4px;
  }
  .story-text {
    font-family: "Cormorant Garamond", serif;
    font-style: italic;
    font-weight: 500;
    font-size: 20.5px;
    line-height: 1.2;
    color: var(--cream);
    text-align: justify;
    margin: 0;
  }
  .age-mark {
    position: absolute;
    left: 500px;
    top: 648px;
    width: 190px;
    text-align: center;
    font-family: "Cormorant Garamond", serif;
    font-weight: 600;
    color: var(--gold);
  }
  .age-row {
    display: flex;
    align-items: center;
    justify-content: center;
    gap: 12px;
    font-size: 17px;
  }
  .age-years {
    width: 78px;
    height: 78px;
    border: 4px solid var(--gold);
    border-radius: 50%;
    box-sizing: border-box;
    display: flex;
    align-items: center;
    justify-content: center;
    font-size: 46px;
    line-height: 1;
  }
  .age-caption {
    font-size: 15px;
    letter-spacing: 0.5px;
    margin-top: 6px;
  }
  .origin {
    position: absolute;
    left: 480px;
    top: 800px;
    width: 230px;
    text-align: center;
    font-family: "Cormorant Garamond", serif;
    font-style: italic;
    font-size: 17px;
    line-height: 1.3;
    color: var(--gold-soft);
  }
</style>
</head>
<body>
  <main class="canvas">
    <section class="label">
      <svg class="label-shapes" width="830" height="892" viewBox="0 0 830 892" aria-hidden="true">
        <!-- lower panel -->
        <path d="M35,240 H780 V862 Q780,892 750,892 H65 Q35,892 35,862 Z" fill="var(--ink)"/>
        <path d="M48,250 H767 V858 Q767,878 747,878 H68 Q48,878 48,858 Z" fill="none" stroke="var(--gold)" stroke-width="4"/>
        <!-- top banner -->
        <path d="M0,55 Q415,-10 830,55 L830,258 Q415,205 0,258 Z" fill="var(--ink)"/>
        <path d="M14,64 Q415,6 816,64 L816,244 Q415,194 14,244 Z" fill="none" stroke="var(--gold)" stroke-width="4"/>
        <!-- product type tab -->
        <rect x="235" y="182" width="363" height="78" fill="var(--ink)"/>
        <rect x="247" y="192" width="339" height="58" fill="none" stroke="var(--gold)" stroke-width="4"/>
      </svg>

      <div class="brand-name">Thornwick Cove</div>
      <div class="product-type">Gold Rum</div>

      <svg class="emblem-art" viewBox="0 0 375 610" role="img" aria-label="Carved tribal emblem artwork in gold on black">
        <defs>
          <linearGradient id="emblemTone" x1="0" y1="0" x2="1" y2="1">
            <stop offset="0" stop-color="var(--gold)" stop-opacity="0.85"/>
            <stop offset="1" stop-color="var(--gold-deep)" stop-opacity="0.85"/>
          </linearGradient>
        </defs>
        <rect width="375" height="610" fill="url(#emblemTone)"/>
      </svg>

      <div class="story">
        <p class="story-kicker">CARIBBEAN STYLE RUM</p>
        <p class="story-text">An Award winning, silky smooth Caribbean style Rum, complex and full-bodied. Barrel aged and bottled by hand in Golden Bay, New Zealand.</p>
      </div>

      <div class="age-mark">
        <div class="age-row">
          <span>YRS</span>
          <span class="age-years">14</span>
          <span>OLD</span>
        </div>
        <div class="age-caption">BARREL AGED</div>
      </div>

      <div class="origin">
        Golden Bay, New Zealand<br>
        40% ALC/VOL 700 mL
      </div>
    </section>
  </main>
</body>
</html>
```